Local Flower Farm Needs Business Card Design

I need business cards designed for a flower farm based in Eudora, Kansas.
Business Info:
We are a local cut flower farm located in Eudora, Kansas, founded by Darla Hoffstrom. What started as a passion for agriculture and search for more joy in daily life has blossomed into a small business dedicated to providing the community with beautiful, fresh, and sustainable flowers. We specialize in local, seasonal blooms, ensuring that every petal reflects the care and dedication we pour into our craft. Our mission is to deliver the highest quality flowers directly to our customers through local farmers markets and to florists who share our commitment to sustainability. Join us in celebrating the beauty of nature, one bloom at a time!
Contact Details:
Darla Hoffstrom
Owner
Phone 913-555-0147
Facebook: Lorabelle Quinn Blossoms
Instagram: @LorabelleQuinnBlossoms
Website: LorabelleQuinnBlossoms.example
Target Market(s)
Wholesale to Florists and Direct to Consumer via Farmers Market
Industry/Entity Type
Florist, Farm
Contact Information for Business Card
Name, Contact Info, Logo
Look and feel

```html
<!DOCTYPE html>
<html lang="en">
<head>
<meta charset="utf-8">
<title>Lorabelle Quinn Blossoms — Business Card</title>
<link rel="stylesheet" href="https://fonts.googleapis.com/css2?family=Playfair+Display:wght@400;700&display=swap">
<style>
  :root {
    --page-bg: #e4e6e5;
    --card-bg: #d8f5ee;
    --ink: #2e2e2e;
    --logo-ink: #11292d;
    --petal: #f2b9c6;
    --sage: #a8bd98;
    --eucalyptus: #8fa79a;
  }
  html, body {
    margin: 0;
    padding: 0;
    width: 900px;
    height: 1200px;
    overflow: hidden;
    background: var(--page-bg);
    font-family: "Playfair Display", Georgia, serif;
  }
  .canvas { position: relative; width: 900px; height: 1200px; }
  .card {
    position: absolute;
    left: 152px;
    width: 605px;
    background: var(--card-bg);
    overflow: hidden;
    box-shadow: 0 6px 18px rgba(0,0,0,0.18);
  }
  .card-front { top: 233px; height: 328px; }
  .card-back { top: 648px; height: 341px; }

  .floral-art { position: absolute; inset: 0; width: 100%; height: 100%; }

  .contact-block { position: absolute; left: 29px; top: 96px; color: var(--ink); }
  .holder-name { margin: 0; font-size: 25px; font-weight: 700; line-height: 1.2; }
  .holder-role { margin: 4px 0 0; font-size: 17px; font-weight: 400; }
  .contact-list { list-style: none; margin: 20px 0 0; padding: 0; }
  .contact-list li {
    display: flex; align-items: center; gap: 11px;
    font-size: 17px; height: 28px;
  }
  .contact-icon { width: 18px; height: 18px; flex: none; }

  .brand-mark {
    position: absolute;
    display: flex; align-items: center; justify-content: center;
    border: 1px solid var(--logo-ink);
    border-radius: 50%;
    color: var(--logo-ink);
    text-align: center;
    font-family: "Playfair Display", Georgia, serif;
    font-weight: 400;
    letter-spacing: 0.12em;
    text-transform: uppercase;
    line-height: 1.5;
  }
  .brand-mark-front { left: 320px; top: 62px; width: 198px; height: 198px; font-size: 15px; }
  .brand-mark-back { left: 208px; top: 39px; width: 206px; height: 206px; font-size: 16px; }
</style>
</head>
<body>
<main class="canvas">

  <section class="card card-front" aria-label="Business card front">
    <svg class="floral-art" viewBox="0 0 605 328" role="img" aria-label="Watercolour-style border of pink sweet-pea blossoms, eucalyptus leaves and baby's breath along the right edge">
      <defs>
        <linearGradient id="front-floral" x1="0" y1="0" x2="1" y2="1">
          <stop offset="0" stop-color="#f2c4cf"/>
          <stop offset="0.5" stop-color="#a9bd9b"/>
          <stop offset="1" stop-color="#8fa79a"/>
        </linearGradient>
      </defs>
      <path d="M370 0 H605 V328 H360 C400 300 470 290 500 250 C520 200 500 150 530 110 C500 60 430 40 370 0 Z" fill="url(#front-floral)" opacity="0.55"/>
    </svg>

    <div class="contact-block">
      <h1 class="holder-name">Darla Hoffstrom</h1>
      <p class="holder-role">Owner</p>
      <ul class="contact-list">
        <li>
          <svg class="contact-icon" viewBox="0 0 24 24" aria-hidden="true"><path d="M6.6 10.8a15.1 15.1 0 0 0 6.6 6.6l2.2-2.2a1 1 0 0 1 1-.25 11.4 11.4 0 0 0 3.6.57 1 1 0 0 1 1 1V20a1 1 0 0 1-1 1A17 17 0 0 1 3 4a1 1 0 0 1 1-1h3.5a1 1 0 0 1 1 1c0 1.25.2 2.45.57 3.57a1 1 0 0 1-.25 1z" fill="#2e2e2e"/></svg>
          <span>913-555-0147</span>
        </li>
        <li>
          <svg class="contact-icon" viewBox="0 0 24 24" aria-hidden="true"><circle cx="12" cy="12" r="10" fill="none" stroke="#2e2e2e" stroke-width="2"/><ellipse cx="12" cy="12" rx="4" ry="10" fill="none" stroke="#2e2e2e" stroke-width="1.6"/><path d="M2 12h20" stroke="#2e2e2e" stroke-width="1.6"/></svg>
          <span>LorabelleQuinnBlossoms.example</span>
        </li>
        <li>
          <svg class="contact-icon" viewBox="0 0 24 24" aria-hidden="true"><circle cx="12" cy="12" r="10" fill="#2e2e2e"/></svg>
          <span>Lorabelle Quinn Blossoms</span>
        </li>
        <li>
          <svg class="contact-icon" viewBox="0 0 24 24" aria-hidden="true"><rect x="2" y="2" width="20" height="20" rx="5" fill="#2e2e2e"/></svg>
          <span>@LorabelleQuinnBlossoms</span>
        </li>
      </ul>
    </div>

    <div class="brand-mark brand-mark-front">Lorabelle<br>Quinn<br>Blossoms</div>
  </section>

  <section class="card card-back" aria-label="Business card back">
    <svg class="floral-art" viewBox="0 0 605 341" role="img" aria-label="Watercolour-style meadow of pink sweet-pea blossoms, sage leaves and baby's breath framing the lower edge and both sides">
      <defs>
        <linearGradient id="back-floral" x1="0" y1="0" x2="0" y2="1">
          <stop offset="0" stop-color="#f2c4cf"/>
          <stop offset="0.6" stop-color="#e9b8c3"/>
          <stop offset="1" stop-color="#a3b995"/>
        </linearGradient>
      </defs>
      <path d="M0 80 C60 90 100 140 110 220 C160 250 250 250 300 260 C360 250 440 250 500 220 C510 150 560 90 605 80 V341 H0 Z" fill="url(#back-floral)" opacity="0.55"/>
    </svg>

    <div class="brand-mark brand-mark-back">Lorabelle<br>Quinn<br>Blossoms</div>
  </section>

</main>
</body>
</html>
```